Info about Getting Rid of Items That People No Longer Want or Need and Would Rather Have the Cash

We need a flyer made to pass out to potential customers describing what it is that we do. We would like for it to be a one page front and back flyer.
Our company helps people who are downsizing or getting rid of items that they no longer want and are unsure of their value. Most Millennials have no interest in their parents items--whether that be art, sterling flatware, jewelry, decorative items or collectibles. On top of that the market is slowing turning as there is more 'stuff" on the market than ever before and less buyers.
We have included some images as examples. For instance: a newspaper headline showing "Millennials Don't Want Your Stuff". In one of the small columns below there could be a picture of an Felix Dunmore painting with a caption reading "Man Buys Original Dunmore for $20 in Garage Sale". Or something like that.
We are open to suggestions and encourage your creativity. These are just examples of what we came up with. These issues, kids not wanting their parents stuff and worry about squandering something special because they didn't know what it is and what its worth are big concerns.
On the back page we are thinking about using a 5 step process to simplify what we do.
Below is a rough example of the 5 steps.
1) Schedule Free In-Home Visit
Please contact us to schedule an appointment
2) Questions, Answers and Facts
We will answer any questions you have and ask you enough questions to make sure we know what your goals are. We will also inform you about market trends and other information related to downsizing
3) The Tour and The Treasure Hunt
You will take us on a tour of your home and point out items you are selling. We will take pictures, notes and point out any treasures that you may not realize you have.
4) Research, Research, Research
We take our notes and photographs back to research your items. Then we will check with our network of experts, dealers and buyers across the country to determine the best market.
5) The Game Plan
We will go over our findings with you. Then we will discuss ways to sell the items to get the highest return.
We have also attached sample images of our business card. We will also want to include our contact information:
Gordon Pellham
555-382-9170
info@gordonapellham.example
www.gordonapellham.example
Target Market(s)
Elderly People or people downsizing
Industry/Entity Type
Cash
Font styles to use
Colors
Designer to choose colors to be used in the design.
Look and feel

```html
<!DOCTYPE html>
<html lang="en">
<head>
<meta charset="utf-8">
<title>Downsizing Flyer – Front and Back</title>
<link rel="stylesheet" href="https://fonts.googleapis.com/css2?family=Bebas+Neue&family=Oswald:wght@500;600&family=Lato:wght@400;700&display=swap">
<style>
  :root {
    --backdrop: #3a3a3a;
    --paper: #f4f4f4;
    --paper-shade: #dcdcdc;
    --ink: #151515;
    --gold: #b5781d;
    --gold-light: #e09a2e;
    --gold-deep: #a8742a;
    --brown-dark: #3a2415;
    --brown-mid: #6b4a22;
    --contact-grey: #c9c9c9;
    --white: #ffffff;
  }
  * { box-sizing: border-box; margin: 0; padding: 0; }
  html, body {
    width: 1200px; height: 1200px; overflow: hidden;
    background: var(--backdrop);
  }
  .canvas { position: relative; width: 1200px; height: 1200px; }

  .flyer {
    position: absolute; top: 233px; width: 524px; height: 736px;
    overflow: hidden; box-shadow: 0 6px 18px rgba(0,0,0,.45);
  }
  .flyer--front { left: 40px; background: linear-gradient(180deg, var(--paper) 0%, var(--paper-shade) 80%); }
  .flyer--back  { left: 638px; background: var(--paper); }

  /* Front */
  .headline {
    position: absolute; left: 54px; top: 22px; z-index: 2;
    font-family: "Bebas Neue", "Oswald", sans-serif; font-weight: 400;
    font-size: 74px; line-height: 64px; color: var(--ink); letter-spacing: .5px;
    white-space: nowrap;
  }
  .headline__accent { color: var(--gold); }
  .portrait-photo {
    position: absolute; left: 128px; top: 150px; width: 280px; height: 460px;
    background: linear-gradient(180deg, #b99a86 0%, #8c7466 22%, #3d3f40 30%, #2b2d2e 100%);
    border-radius: 120px 120px 0 0; z-index: 1;
  }
  .story-band {
    position: absolute; left: 0; right: 0; bottom: 0; height: 128px;
    background: linear-gradient(90deg, var(--gold-deep) 0%, var(--gold-light) 55%, #b9842f 100%);
    z-index: 2;
  }
  .story-band__step {
    position: absolute; left: 0; top: 590px; width: 190px; height: 20px;
    background: var(--gold-deep); z-index: 2;
  }
  .artwork-frame {
    position: absolute; left: 24px; top: 574px; width: 132px; height: 132px;
    border: 3px solid var(--white); z-index: 3;
    background: linear-gradient(135deg, #46b3ad 0%, #3aa39e 100%);
    box-shadow: 0 3px 8px rgba(0,0,0,.35);
  }
  .story-caption {
    position: absolute; left: 182px; top: 630px; z-index: 3;
    font-family: "Bebas Neue", "Oswald", sans-serif; font-weight: 400;
    font-size: 36px; line-height: 38px; color: var(--ink); white-space: nowrap;
  }
  .story-caption__hi { color: var(--white); }

  /* Back */
  .process-title {
    position: absolute; left: 0; right: 0; top: 22px; text-align: center;
    font-family: "Bebas Neue", "Oswald", sans-serif; font-weight: 400;
    font-size: 30px; line-height: 26px; color: var(--ink);
  }
  .process-title__line2 {
    display: inline-block; border-bottom: 3px solid var(--gold-deep); padding-bottom: 2px;
  }
  .steps { position: absolute; left: 22px; top: 96px; width: 480px; height: 490px; }
  .steps__bands { position: absolute; inset: 0; }
  .step { position: absolute; left: 0; width: 480px; height: 88px; color: var(--white); }
  .step__label {
    position: absolute; width: 60px;
    font-family: "Bebas Neue", "Oswald", sans-serif; font-weight: 400; line-height: 1;
  }
  .step__word { display: block; font-size: 20px; }
  .step__num { display: block; font-size: 40px; margin-top: 2px; }
  .step__body { position: absolute; font-family: "Lato", sans-serif; }
  .step__title {
    font-family: "Bebas Neue", "Oswald", sans-serif; font-weight: 400; font-size: 20px;
    line-height: 20px; white-space: nowrap; margin-bottom: 2px;
  }
  .step__text { font-size: 8.4px; line-height: 10.4px; }
  .step__text--justify { text-align: justify; }
  .step__icon { position: absolute; }

  .contact {
    position: absolute; left: 22px; top: 613px; width: 480px; height: 101px;
    background: var(--contact-grey); font-family: "Lato", sans-serif; color: var(--ink);
  }
  .contact__tab {
    position: absolute; left: 186px; top: -9px; width: 120px; height: 20px;
    background: var(--brown-dark); color: var(--white);
    font-family: "Oswald", sans-serif; font-weight: 500; font-size: 9.5px;
    line-height: 20px; text-align: center; white-space: nowrap;
    clip-path: polygon(6% 0, 94% 0, 100% 100%, 0 100%);
  }
  .contact__name { position: absolute; left: 22px; top: 22px; font-size: 12.5px; }
  .contact__list { position: absolute; list-style: none; white-space: nowrap; }
  .contact__list li { display: flex; align-items: center; gap: 9px; height: 20px; }
  .contact__list--phone { left: 22px; top: 48px; font-size: 12.5px; }
  .contact__list--web { left: 180px; top: 49px; font-size: 9.5px; font-weight: 700; }
  .contact__list--social { left: 372px; top: 42px; font-size: 10.5px; }
  .contact__list--social li { height: 15px; gap: 7px; }
  .contact__icon { width: 12px; height: 12px; flex: none; }
  .contact__dot { width: 9px; height: 9px; border-radius: 50%; background: var(--gold-deep); flex: none; }
</style>
</head>
<body>
<main class="canvas">

  <!-- Front side -->
  <section class="flyer flyer--front">
    <h1 class="headline"><span class="headline__accent">Millennials</span> Don't<br>Want Your Stuff</h1>
    <div class="portrait-photo" role="img" aria-label="Photo of the company owner in a dark suit standing with arms crossed"></div>
    <div class="story-band__step"></div>
    <div class="story-band"></div>
    <div class="artwork-frame" role="img" aria-label="Colourful pop-art portrait painting in teal, yellow and pink"></div>
    <p class="story-caption">Man buys original <span class="story-caption__hi">Dunmore</span><br>for <span class="story-caption__hi">$20</span> in garage sale</p>
  </section>

  <!-- Back side -->
  <section class="flyer flyer--back">
    <h2 class="process-title">5 Step Process<br><span class="process-title__line2">To Simplify What We Do</span></h2>

    <div class="steps">
      <svg class="steps__bands" width="480" height="490" viewBox="0 0 480 490" aria-hidden="true">
        <defs>
          <linearGradient id="band-gold-left" gradientUnits="userSpaceOnUse" x1="0" y1="0" x2="480" y2="0">
            <stop offset="0" stop-color="#a87a34"/>
            <stop offset=".55" stop-color="#6b4a22"/>
            <stop offset="1" stop-color="#3a2415"/>
          </linearGradient>
          <linearGradient id="band-gold-right" gradientUnits="userSpaceOnUse" x1="0" y1="0" x2="480" y2="0">
            <stop offset="0" stop-color="#3a2415"/>
            <stop offset=".45" stop-color="#6b4a22"/>
            <stop offset="1" stop-color="#a87a34"/>
          </linearGradient>
        </defs>
        <polygon fill="url(#band-gold-left)"  points="0,0 480,0 480,88 435,88 380,112 325,88 0,88"/>
        <polygon fill="url(#band-gold-right)" points="0,100 323,100 380,124 437,100 480,100 480,188 155,188 100,212 45,188 0,188"/>
        <polygon fill="url(#band-gold-left)"  points="0,200 43,200 100,224 157,200 480,200 480,288 435,288 380,312 325,288 0,288"/>
        <polygon fill="url(#band-gold-right)" points="0,300 323,300 380,324 437,300 480,300 480,388 155,388 100,412 45,388 0,388"/>
        <polygon fill="url(#band-gold-left)"  points="0,400 43,400 100,424 157,400 480,400 480,488 0,488"/>
      </svg>

      <!-- Step 1 -->
      <div class="step" style="top:0">
        <div class="step__label" style="left:21px;top:16px"><span class="step__word">STAPE</span><span class="step__num">01</span></div>
        <div class="step__body" style="left:111px;top:26px;width:220px">
          <h3 class="step__title">SCHEDULE FREE IN-HOME VISIT</h3>
          <p class="step__text" style="font-size:10px">Please contact us to schedule an appointment</p>
        </div>
        <svg class="step__icon" style="left:364px;top:20px" width="56" height="56" viewBox="0 0 56 56" fill="none" stroke="#fff" stroke-width="3">
          <rect x="3" y="8" width="42" height="38" rx="3"/>
          <line x1="3" y1="17" x2="45" y2="17"/>
          <line x1="13" y1="3" x2="13" y2="12"/><line x1="35" y1="3" x2="35" y2="12"/>
          <rect x="9" y="23" width="6" height="5" fill="#fff" stroke="none"/>
          <rect x="19" y="23" width="6" height="5" fill="#fff" stroke="none"/>
          <rect x="9" y="33" width="6" height="5" fill="#fff" stroke="none"/>
          <circle cx="41" cy="42" r="11" fill="#3a2415"/>
          <polyline points="41,36 41,42 46,45"/>
        </svg>
      </div>

      <!-- Step 2 -->
      <div class="step" style="top:100px">
        <svg class="step__icon" style="left:32px;top:20px" width="70" height="52" viewBox="0 0 70 52" fill="none" stroke="#fff" stroke-width="3.5">
          <path d="M24 4a20 18 0 1 0 0 36c3 0 6-.6 8-1.6L42 44l-3-9a18 16 0 0 0 5-13A20 18 0 0 0 24 4z"/>
          <text x="16" y="30" fill="#fff" stroke="none" font-family="Oswald, sans-serif" font-size="24" font-weight="600">?</text>
          <path d="M50 16a16 14 0 0 1 0 28c-2 0-4-.3-6-1l-8 5 2-7" />
          <circle cx="45" cy="30" r="2" fill="#fff" stroke="none"/><circle cx="52" cy="30" r="2" fill="#fff" stroke="none"/><circle cx="59" cy="30" r="2" fill="#fff" stroke="none"/>
        </svg>
        <div class="step__body" style="left:160px;top:16px;width:205px">
          <h3 class="step__title">QUESTIONS, ANSWERS AND FACTS</h3>
          <p class="step__text step__text--justify">We will answer any questions you have and ask you enough questions to make sure we know what your goals are. We will also inform you about market trends and other information related to downsizing</p>
        </div>
        <div class="step__label" style="left:422px;top:18px"><span class="step__word">STAPE</span><span class="step__num">02</span></div>
      </div>

      <!-- Step 3 -->
      <div class="step" style="top:200px">
        <div class="step__label" style="left:21px;top:16px"><span class="step__word">STAPE</span><span class="step__num">03</span></div>
        <div class="step__body" style="left:110px;top:20px;width:205px">
          <h3 class="step__title">THE TOUR AND THE TREASURE HUNT</h3>
          <p class="step__text">You will take us on a tour of your home and point out items you are selling. We will take pictures, notes and point out any treasures that you may not realize you have.</p>
        </div>
        <svg class="step__icon" style="left:366px;top:14px" width="60" height="60" viewBox="0 0 24 24" fill="#fff">
          <path d="M21.5 2.5c-.8-.8-2.2-.7-3 .1L15 6.1 5.5 3.5 3.8 5.2l7.6 4.6-3.7 3.7-2.9-.4-1.3 1.3 3.4 2 2 3.4 1.3-1.3-.4-2.9 3.7-3.7 4.6 7.6 1.7-1.7L17.9 9l3.5-3.5c.8-.8.9-2.2.1-3z"/>
        </svg>
      </div>

      <!-- Step 4 -->
      <div class="step" style="top:300px">
        <svg class="step__icon" style="left:34px;top:22px" width="68" height="50" viewBox="0 0 68 50" fill="none" stroke="#fff" stroke-width="3.2">
          <path d="M4 10c10-4 20-4 30 2 10-6 20-6 30-2v32c-10-4-20-4-30 2-10-6-20-6-30-2z"/>
          <line x1="34" y1="12" x2="34" y2="44"/>
          <circle cx="36" cy="22" r="11" fill="#3a2415"/>
          <line x1="44" y1="30" x2="56" y2="43" stroke-width="5" stroke-linecap="round"/>
        </svg>
        <div class="step__body" style="left:160px;top:16px;width:205px">
          <h3 class="step__title">RESEARCH, RESEARCH, RESEARCH</h3>
          <p class="step__text step__text--justify">We will answer any questions you have and ask you enough questions to make sure we know what your goals are. We will also inform you about market trends and other information related to downsizing</p>
        </div>
        <div class="step__label" style="left:422px;top:18px"><span class="step__word">STAPE</span><span class="step__num">04</span></div>
      </div>

      <!-- Step 5 -->
      <div class="step" style="top:400px">
        <div class="step__label" style="left:21px;top:26px"><span class="step__word">STAPE</span><span class="step__num">05</span></div>
        <div class="step__body" style="left:119px;top:36px;width:210px">
          <h3 class="step__title">THE GAME PLAN</h3>
          <p class="step__text">We will go over our findings with you. Then we will discuss ways to sell the items to get the highest return.</p>
        </div>
        <svg class="step__icon" style="left:378px;top:22px" width="46" height="52" viewBox="0 0 46 52" fill="none" stroke="#fff" stroke-width="3">
          <rect x="3" y="3" width="32" height="46" rx="2"/>
          <line x1="9" y1="12" x2="12" y2="12"/><line x1="16" y1="12" x2="29" y2="12"/>
          <line x1="9" y1="20" x2="12" y2="20"/><line x1="16" y1="20" x2="29" y2="20"/>
          <line x1="9" y1="28" x2="12" y2="28"/><line x1="16" y1="28" x2="26" y2="28"/>
          <line x1="9" y1="36" x2="12" y2="36"/><line x1="16" y1="36" x2="22" y2="36"/>
          <path d="M42 24 28 44l-4 3 1-5 14-20z" fill="#3a2415"/>
        </svg>
      </div>
    </div>

    <div class="contact">
      <div class="contact__tab">CONTACT INFORMATION :</div>
      <p class="contact__name">Gordon Pellham</p>
      <ul class="contact__list contact__list--phone">
        <li><svg class="contact__icon" viewBox="0 0 24 24" fill="#a8742a"><path d="M6.6 10.8a15.1 15.1 0 0 0 6.6 6.6l2.2-2.2c.3-.3.7-.4 1-.2 1.1.4 2.3.6 3.6.6.6 0 1 .4 1 1V20c0 .6-.4 1-1 1A17 17 0 0 1 3 4c0-.6.4-1 1-1h3.5c.6 0 1 .4 1 1 0 1.3.2 2.5.6 3.6.1.3 0 .7-.2 1z"/></svg>555-382-9170</li>
        <li><svg class="contact__icon" viewBox="0 0 24 24" fill="#a8742a"><path d="M6.6 10.8a15.1 15.1 0 0 0 6.6 6.6l2.2-2.2c.3-.3.7-.4 1-.2 1.1.4 2.3.6 3.6.6.6 0 1 .4 1 1V20c0 .6-.4 1-1 1A17 17 0 0 1 3 4c0-.6.4-1 1-1h3.5c.6 0 1 .4 1 1 0 1.3.2 2.5.6 3.6.1.3 0 .7-.2 1z"/></svg>555-382-9174</li>
      </ul>
      <ul class="contact__list contact__list--web">
        <li><svg class="contact__icon" viewBox="0 0 24 24" fill="none" stroke="#a8742a" stroke-width="2.4"><rect x="2" y="5" width="20" height="14" rx="1"/><polyline points="2,6 12,13 22,6"/></svg>info@gordonapellham.example</li>
        <li><svg class="contact__icon" viewBox="0 0 24 24" fill="none" stroke="#a8742a" stroke-width="2"><circle cx="12" cy="12" r="10"/><ellipse cx="12" cy="12" rx="4.5" ry="10"/><line x1="2" y1="12" x2="22" y2="12"/></svg>www.gordonapellham.example</li>
      </ul>
      <ul class="contact__list contact__list--social">
        <li><span class="contact__dot"></span>/gordonpellham</li>
        <li><span class="contact__dot"></span>/gordonpellham</li>
        <li><span class="contact__dot"></span>/gordonpellham</li>
      </ul>
    </div>
  </section>

</main>
</body>
</html>
```